Re make of the website. A fine diamond jeweller based in Melbourne Australia.

We would like the website redesigned. http://peterlindvale.com.au/

Current website is very dated and we would like it re made and updated. An example of what we would like is https://www.tessagorblin.com/au/ or https://brookfinch.co.nz/

We sell high end diamond jewellery and the main purpose of the website will be to get people to enquire and make a booking to design a ring/meet with the experts in store. There is also a small online store.

Target Market(s)

High Affluence 25-70

Number of Pages Required

5+ page

Font styles to use
Sans Serif
Other font styles liked:
• Muli Fine

Requirements
Must have
• All the current features on the website
• Very elegant
• Main cover image
• Lots of lifestyle imagers - less blank space
• 1. Online Shop
• 2. Home page
• 3. Contact us/enquiry page
• 4. Jewellery Page
• 5. About page

```html
<!DOCTYPE html>
<html lang="en">
<head>
<meta charset="utf-8">
<title>Peter Lindvale — High End Diamond Jewellery</title>
<link rel="stylesheet" href="https://fonts.googleapis.com/css2?family=Mulish:wght@300;400;600;700&display=swap">
<style>
  :root {
    --ink: #2b2b2b;
    --muted: #6f6f6f;
    --bronze: #b8977c;
    --bronze-soft: #c5ab95;
    --topbar: #f7f7f7;
    --line: #e2e2e2;
    --navy: #2a2f38;
    --slate: #2f3540;
    --sky: #7fb0cf;
    --lavender: #dcdfee;
    --sale-band: #f4f4f4;
    --white: #ffffff;
  }
  * { box-sizing: border-box; margin: 0; padding: 0; }
  html, body { width: 1200px; height: 2287px; overflow: hidden; }
  body { position: relative; background: var(--white); font-family: "Mulish", sans-serif; color: var(--ink); }
  .abs { position: absolute; }

  /* top bar */
  .topbar { left: 0; top: 0; width: 1200px; height: 38px; background: var(--topbar); border-bottom: 1px solid var(--line); }
  .topbar-link { top: 0; height: 38px; line-height: 38px; font-size: 12px; letter-spacing: 1px; color: var(--muted); border-left: 1px solid var(--line); padding: 0 16px; }
  .cart-count { left: 1081px; top: 2px; width: 18px; height: 16px; background: #cfcfcf; color: #fff; font-size: 9px; text-align: center; line-height: 16px; }

  /* nav */
  .nav { left: 0; top: 38px; width: 1200px; height: 76px; background: var(--white); }
  .brand { display: flex; align-items: center; gap: 8px; }
  .brand-mark { width: 16px; height: 16px; background: var(--ink); }
  .brand-name { font-size: 15px; font-weight: 400; letter-spacing: 1px; color: var(--ink); }
  .nav-links { left: 297px; top: 70px; display: flex; gap: 26px; font-size: 12px; letter-spacing: 1px; color: var(--ink); }

  /* hero */
  .hero { left: 0; top: 114px; width: 1200px; height: 504px; background: radial-gradient(ellipse at 60% 40%, #f2f2f2, #d9d9d9 80%); }
  .hero-kicker { left: 200px; top: 241px; font-size: 13px; letter-spacing: 2px; color: var(--bronze); font-weight: 600; }
  .hero-title { left: 198px; top: 268px; font-size: 52px; line-height: 64px; font-weight: 300; color: var(--bronze); }
  .hero-sub { left: 200px; top: 414px; font-size: 24px; font-weight: 400; color: var(--ink); letter-spacing: 0.5px; }
  .btn-book { left: 200px; top: 471px; width: 125px; height: 38px; background: var(--bronze); color: #fff; font-size: 12px; letter-spacing: 1.5px; text-align: center; line-height: 38px; }
  .hero-product { left: 716px; top: 267px; width: 298px; height: 229px; border-radius: 50% 50% 40% 40%; background: radial-gradient(circle at 50% 35%, #ffffff, #c9ccd6 55%, #3a3d56 85%); }
  .hero-dots { left: 562px; top: 578px; display: flex; gap: 12px; }
  .hero-dots span { width: 10px; height: 10px; border: 1.5px solid var(--ink); border-radius: 50%; }

  /* feature photos */
  .photo { overflow: hidden; }
  .feature-caption { font-size: 27px; line-height: 32px; font-weight: 300; color: var(--ink); }
  .learn-tag { background: var(--bronze-soft); color: var(--ink); font-size: 10px; letter-spacing: 1px; display: flex; align-items: center; }

  /* tiles */
  .tile-label { font-size: 10px; letter-spacing: 1px; font-weight: 700; color: #fff; }
  .tile-text { font-size: 20px; line-height: 30px; font-weight: 300; color: #fff; }
  .tile-meta { font-size: 10px; color: #fff; display: flex; align-items: center; gap: 5px; }

  /* story */
  .story { left: 0; top: 1266px; width: 1200px; height: 373px; background: var(--lavender); }
  .story-text { left: 625px; top: 1334px; width: 200px; font-size: 15px; line-height: 24.5px; font-style: italic; font-weight: 400; color: var(--ink); }
  .founder-name { left: 851px; top: 1462px; font-size: 11px; font-weight: 700; color: var(--ink); }
  .founder-role { left: 851px; top: 1484px; font-size: 11px; font-style: italic; color: var(--muted); }

  /* lifestyle */
  .karat-panel { left: 0; top: 1647px; width: 293px; height: 252px; background: var(--bronze-soft); overflow: hidden; }
  .karat-title { left: 126px; top: 1705px; font-size: 20px; line-height: 24px; font-weight: 300; color: #fff; }
  .karat-big { left: -8px; top: 1770px; font-size: 160px; font-weight: 700; line-height: 1; color: rgba(255,255,255,0.35); letter-spacing: -4px; }

  /* sale */
  .sale-band { left: 0; top: 1899px; width: 1200px; height: 126px; background: var(--sale-band); }
  .sale-lead { left: 393px; top: 1945px; font-size: 26px; font-weight: 400; color: var(--ink); }
  .sale-big { left: 633px; top: 1918px; font-size: 64px; font-weight: 300; color: var(--ink); letter-spacing: 2px; }

  /* footer */
  .footer-heading { font-size: 13px; letter-spacing: 1.5px; color: var(--ink); line-height: 26px; }
  .footer-list { list-style: none; font-size: 12px; line-height: 25px; color: var(--muted); font-weight: 300; }
  .copyright { left: 125px; top: 2140px; font-size: 11px; line-height: 20px; color: var(--muted); }
  .btn-ok { left: 1037px; top: 2112px; width: 38px; height: 36px; background: #9a9a9a; color: #fff; font-size: 11px; text-align: center; line-height: 36px; }
</style>
</head>
<body>

<!-- Top bar -->
<div class="abs topbar"></div>
<div class="abs topbar-link" style="left:893px;">LOGIN</div>
<div class="abs topbar-link" style="left:967px; border-right:0;">MY CART</div>
<svg class="abs" style="left:1045px;top:9px" width="26" height="22" viewBox="0 0 26 22" fill="none" stroke="#2b2b2b" stroke-width="1.4">
  <path d="M1 2h4l3 12h13l3-9H7"/><circle cx="10" cy="18" r="1.6"/><circle cx="19" cy="18" r="1.6"/>
</svg>
<div class="abs cart-count">0</div>

<!-- Navigation -->
<header class="abs nav"></header>
<div class="abs brand" style="left:98px;top:66px;">
  <span class="brand-mark"></span><span class="brand-name">PETER LINDVALE</span>
</div>
<nav class="abs nav-links">
  <span>HOME</span><span>SHOP</span><span>JEWELLERY</span><span>ABOUT US</span><span>CONTACT US</span>
</nav>
<svg class="abs" style="left:1052px;top:66px" width="18" height="18" viewBox="0 0 18 18" fill="none" stroke="#2b2b2b" stroke-width="1.5">
  <circle cx="7.5" cy="7.5" r="6"/><path d="M12 12l5 5"/>
</svg>

<!-- Hero -->
<section class="abs hero" role="img" aria-label="Soft grey marble backdrop"></section>
<div class="abs hero-kicker">PETER LINDVALE</div>
<h1 class="abs hero-title">High End<br>Diamond Jewellery</h1>
<div class="abs hero-sub">FINER JEWELLERY SINCE 1923</div>
<div class="abs btn-book">BOOK NOW</div>
<div class="abs hero-product" role="img" aria-label="White gold diamond ring flanked by two blue sapphires"></div>
<svg class="abs" style="left:124px;top:340px" width="28" height="52" viewBox="0 0 28 52" fill="none" stroke="#8a8a8a" stroke-width="1.5"><path d="M26 2L2 26l24 24"/></svg>
<svg class="abs" style="left:1050px;top:340px" width="28" height="52" viewBox="0 0 28 52" fill="none" stroke="#8a8a8a" stroke-width="1.5"><path d="M2 2l24 24L2 50"/></svg>
<div class="abs hero-dots"><span></span><span></span><span></span><span></span></div>

<!-- Feature photos -->
<div class="abs photo" style="left:0;top:622px;width:596px;height:377px;background:linear-gradient(135deg,#d9d3cd,#b9a192 55%,#6e6660);" role="img" aria-label="Two smiling women embracing, one wearing a diamond ring"></div>
<div class="abs learn-tag" style="left:130px;top:898px;width:74px;height:74px;flex-direction:column;align-items:flex-start;justify-content:center;padding-left:8px;line-height:12px;">
  <span>LEARN</span><span>MORE</span>
  <span style="margin-top:10px;display:flex;align-items:center;gap:4px;">
    <svg width="11" height="11" viewBox="0 0 12 12" fill="none" stroke="#2b2b2b"><circle cx="3" cy="6" r="2"/><circle cx="9" cy="2.5" r="2"/><circle cx="9" cy="9.5" r="2"/><path d="M5 5l2-1.5M5 7l2 1.5"/></svg>39
  </span>
</div>
<div class="abs feature-caption" style="left:223px;top:906px;">The Velmarino<br>Noiseless Experience</div>

<div class="abs photo" style="left:604px;top:622px;width:596px;height:377px;background:linear-gradient(135deg,#2a2a2a,#5a4c44 40%,#e9ddd0 70%,#cfc2b6);" role="img" aria-label="Laughing woman in white fur beside a man in a suit, showing an engagement ring"></div>
<div class="abs learn-tag" style="left:630px;top:948px;width:200px;height:24px;justify-content:space-between;padding:0 10px;">
  <span>LEARN MORE</span>
  <span style="display:flex;align-items:center;gap:4px;">
    <svg width="11" height="11" viewBox="0 0 12 12" fill="none" stroke="#2b2b2b"><circle cx="3" cy="6" r="2"/><circle cx="9" cy="2.5" r="2"/><circle cx="9" cy="9.5" r="2"/><path d="M5 5l2-1.5M5 7l2 1.5"/></svg>36
  </span>
</div>
<div class="abs feature-caption" style="left:850px;top:916px;">Special<br>Occasion Rings!</div>

<!-- Product tiles -->
<div class="abs" style="left:0;top:1006px;width:596px;height:251px;background:var(--navy);"></div>
<div class="abs tile-label" style="left:123px;top:1022px;">NEW PRODUCT MARCH, 17</div>
<div class="abs" style="left:98px;top:1060px;width:280px;height:165px;border-radius:45%;background:radial-gradient(circle at 70% 45%,#ffffff,#d8d8d8 18%,#c9a04a 40%,#6d5520 75%,transparent 78%);" role="img" aria-label="Stacked gold rings with a large round diamond"></div>
<div class="abs tile-text" style="left:405px;top:1080px;">Pink diamond<br>bezel with<br>brilliant whites</div>
<div class="abs tile-label" style="left:123px;top:1218px;font-weight:600;">SHOP NOW</div>

<div class="abs" style="left:604px;top:1006px;width:251px;height:251px;background:var(--sky);"></div>
<div class="abs tile-label" style="left:630px;top:1022px;">TOP SELLING MARCH, 17</div>
<div class="abs tile-text" style="left:630px;top:1050px;">Presently a breeze<br>of Gold</div>
<div class="abs" style="left:660px;top:1125px;width:130px;height:85px;border-radius:50%;background:radial-gradient(circle at 50% 35%,#ffffff,#e7e7e7 30%,#c9a14c 60%,transparent 66%);" role="img" aria-label="Gold ring with emerald cut diamond"></div>
<div class="abs tile-meta" style="left:630px;top:1220px;">
  <svg width="16" height="10" viewBox="0 0 16 10" fill="none" stroke="#fff"><path d="M1 5c3-5 11-5 14 0-3 5-11 5-14 0z"/><circle cx="8" cy="5" r="2"/></svg>4 055
  <svg style="margin-left:14px" width="11" height="11" viewBox="0 0 12 12" fill="none" stroke="#fff"><circle cx="3" cy="6" r="2"/><circle cx="9" cy="2.5" r="2"/><circle cx="9" cy="9.5" r="2"/><path d="M5 5l2-1.5M5 7l2 1.5"/></svg>34
</div>
<svg class="abs" style="left:803px;top:1218px" width="26" height="14" viewBox="0 0 26 14" fill="none" stroke="#fff" stroke-width="1.4"><path d="M0 7h24M18 1l6 6-6 6"/></svg>

<div class="abs" style="left:863px;top:1006px;width:337px;height:251px;background:linear-gradient(135deg,var(--slate),#3a414d);"></div>
<div class="abs" style="left:1000px;top:1030px;width:130px;height:227px;background:linear-gradient(180deg,#2a2a2a,#7d8896 50%,#c9ccd0);border-radius:40% 40% 0 0;" role="img" aria-label="Model in a draped grey and blue garment"></div>
<div class="abs tile-label" style="left:890px;top:1022px;">MUST HAVE</div>
<div class="abs tile-text" style="left:886px;top:1148px;">According to her<br>lorem ipsum,<br>following a desire</div>

<!-- Story -->
<section class="abs story"></section>
<div class="abs" style="left:100px;top:1328px;width:496px;height:249px;background:linear-gradient(120deg,#3a2f28,#c2a08e 40%,#e2642c 75%,#c24a1e);" role="img" aria-label="Woman in an orange top raising a champagne glass, wearing a diamond ring"></div>
<p class="abs story-text">Enjoy the experience of ordering a fully handmade diamond ring, and discussing diamond quality and pricing in a highly professional environment. Peter Lindvale manufacture in house and hold a large collection of quality</p>
<div class="abs" style="left:851px;top:1327px;width:125px;height:125px;background:linear-gradient(160deg,#2c2c2c,#8d8d8d 60%,#5c5c5c);" role="img" aria-label="Black and white portrait of the founder"></div>
<div class="abs founder-name">Peter Lindvale Diamonds</div>
<div class="abs founder-role">Founder</div>
<div class="abs" style="left:815px;top:1500px;width:230px;height:80px;background:linear-gradient(90deg,transparent,rgba(43,43,43,0.08),transparent);" role="img" aria-label="Founder's handwritten signature"></div>
<svg class="abs" style="left:1020px;top:1378px" width="34" height="26" viewBox="0 0 34 26" fill="#b7b9c4"><path d="M2 24V12L10 2h5L10 12h5v12zM19 24V12L27 2h5l-5 10h5v12z"/></svg>

<!-- Lifestyle -->
<div class="abs karat-panel"></div>
<div class="abs karat-big">24K</div>
<div class="abs karat-title">Peter Lindvale<br>Diamonds</div>
<div class="abs" style="left:303px;top:1647px;width:293px;height:252px;background:linear-gradient(180deg,#d8d2c2,#a7a08e 45%,#6b8a4a 62%,#d9c76a 85%,#9b9287);" role="img" aria-label="Woman in a yellow patterned skirt at a street event"></div>
<div class="abs" style="left:605px;top:1647px;width:293px;height:252px;background:linear-gradient(180deg,#cfcac0,#8a7a6a 35%,#4a6486 60%,#9a5a2c 80%,#b8b0a4);" role="img" aria-label="Couple walking in denim overalls and a rust dress"></div>
<div class="abs" style="left:909px;top:1647px;width:291px;height:252px;background:linear-gradient(180deg,#5a4e44,#8a7562 40%,#a8652e 60%,#2a2a2a 85%,#8c8780);" role="img" aria-label="Man in a patterned shirt and black trousers on a city street"></div>

<!-- Sale -->
<section class="abs sale-band"></section>
<div class="abs" style="left:244px;top:1918px;width:107px;height:92px;border-radius:50%;background:radial-gradient(circle at 50% 38%,#f4f4f4 0,#e8e0e6 18%,#7a3a4a 36%,#c9a04a 44%,transparent 48%),radial-gradient(ellipse at 50% 82%,#2a2a2a 0,#6a6a6a 30%,transparent 34%);" role="img" aria-label="Diamond cluster ring with pink and gold halo"></div>
<div class="abs sale-lead">Holiday Season!</div>
<div class="abs sale-big">20%&nbsp; SALE</div>

<!-- Footer -->
<div class="abs brand" style="left:125px;top:2078px;">
  <span class="brand-mark"></span><span class="brand-name">PETER LINDVALE</span>
</div>
<div class="abs copyright">© 2017 PETER LINDVALE<br>All Rights Reserved.</div>

<div class="abs" style="left:374px;top:2053px;">
  <div class="footer-heading">SITE MAP</div>
  <ul class="footer-list" style="margin-top:10px;"><li>Home</li><li>Shop</li><li>Jewellery</li><li>About Us</li><li>Contact Us</li></ul>
</div>
<div class="abs" style="left:624px;top:2053px;">
  <div class="footer-heading">HELP</div>
  <ul class="footer-list" style="margin-top:10px;"><li>Contact us</li><li>Track orders</li><li>FAQ</li><li>Shipping info</li></ul>
</div>
<div class="abs" style="left:875px;top:2053px;">
  <div class="footer-heading">SUBSCRIBE<br>TO OUR NEWSLETTER</div>
</div>
<div class="abs" style="left:875px;top:2140px;width:150px;border-bottom:1px solid var(--line);"></div>
<div class="abs btn-ok">OK</div>
<ul class="abs footer-list" style="left:875px;top:2170px;font-size:11px;line-height:21px;"><li>Privacy &amp; Cookies</li><li>Terms &amp; Conditions</li><li>Accessibility</li></ul>

</body>
</html>
```